Powerpoint Presentation (urgent)

We need a powerpoint presentation to accompany our other pitch materials for a really exciting, new project.

It is a project related to gaming.

The presentation should be engaging, professionally done, and be trendy and captivating.

```html
<!DOCTYPE html>
<html lang="en">
<head>
<meta charset="utf-8">
<title>Gaming Pitch Deck – Slide Overview</title>
<link href="https://fonts.googleapis.com/css2?family=Montserrat:wght@400;500;600;700&display=swap" rel="stylesheet">
<style>
:root{
  --red:#c41230;
  --rose:#d4486a;
  --ink:#111111;
  --charcoal:#3b3939;
  --stone:#6b6464;
  --grey:#8a8a8a;
  --mist:#b3b3b3;
  --paper:#ffffff;
  --text:#333333;
}
*{box-sizing:border-box;margin:0;padding:0}
html,body{width:1200px;height:888px;overflow:hidden;background:var(--paper)}
body{position:relative;font-family:"Montserrat",sans-serif;color:var(--text)}
.slide{position:absolute;width:383px;height:216px;background:var(--paper);overflow:hidden;box-shadow:0 0 3px rgba(0,0,0,.25)}
.abs{position:absolute}
.c1{left:8px}.c2{left:408px}.c3{left:808px}
.r1{top:4px}.r2{top:226px}.r3{top:449px}.r4{top:671px}

.slide-title{position:absolute;left:17px;top:17px;font-size:16.5px;font-weight:600;color:var(--ink);letter-spacing:-.2px}
.slide-title::after{content:"";display:block;width:20px;height:2px;background:var(--red);margin-top:2px}
.brand{position:absolute;right:14px;top:24px;display:flex;align-items:center;gap:3px;font-size:7px;font-weight:700;color:var(--red);letter-spacing:.4px}
.brand-dot{width:7px;height:7px;border-radius:50%;background:var(--ink)}
.brand.light .brand-dot{background:var(--paper)}
.footer{position:absolute;left:0;bottom:0;width:100%;height:9px;background:var(--red);color:var(--paper);font-size:3.6px;display:flex;justify-content:space-between;align-items:center;padding:0 5px}
.lead{position:absolute;left:34px;right:34px;font-size:4.6px;line-height:6px;color:var(--grey)}
.tiny{font-size:4.2px;line-height:5.2px;color:var(--mist)}
.label{font-size:6.4px;color:var(--text)}
.photo{position:absolute}

/* divider */
.divider .photo{inset:0;background:linear-gradient(120deg,#2b2b2b 0%,#1c1c1c 45%,#3a3838 70%,#151515 100%)}
.divider-kicker{left:75px;top:112px;font-size:6.5px;color:#ddd}
.divider-title{left:9px;top:120px;font-size:17px;font-weight:600;color:var(--paper)}
.divider-sub{left:55px;top:142px;font-size:8.5px;color:#ddd}

/* mockup */
.mock-band{left:0;top:0;width:100%;height:133px;background:var(--ink)}
.mock-title{left:17px;top:48px;font-size:18px;font-weight:600;line-height:23px;color:var(--paper)}
.mock-screen{left:124px;top:36px;width:136px;height:94px;background:linear-gradient(135deg,#8a8f96,#4b5966 60%,#2d3640);border:4px solid #cfd2d6;border-bottom:none;border-radius:5px 5px 0 0}
.mock-base{left:98px;top:130px;width:190px;height:5px;background:#d7d9dc;border-radius:0 0 6px 6px}
.feature{position:absolute;width:110px}
.feature .label{display:block}
.feature.left{text-align:right}
.ico{position:absolute;width:11px;height:11px;border-radius:50%;background:var(--ink)}

/* video */
.video-title{left:17px;top:30px;font-size:17px;font-weight:600;line-height:17px;color:var(--ink)}
.video-copy{left:17px;top:86px;width:104px}
.video-copy p{margin-bottom:5px}
.monitor{left:120px;top:34px;width:215px;height:160px;background:#cfd1d3;border-radius:4px;padding:5px 5px 15px}
.monitor .photo{position:relative;width:100%;height:100%;background:linear-gradient(135deg,#b8a592,#8c7a68 50%,#5c5148)}
.monitor-neck{left:214px;top:194px;width:28px;height:12px;background:#bfc1c3}
.monitor-foot{left:200px;top:204px;width:56px;height:3px;background:#aeb0b2;border-radius:2px}

/* four boxes */
.box{position:absolute;top:81px;width:70px;height:94px;color:var(--paper);text-align:center;padding-top:21px}
.box .badge{width:13px;height:13px;border-radius:50%;background:var(--paper);margin:0 auto 19px}
.box h4{font-size:4.6px;font-weight:400;margin-bottom:3px}
.box p{font-size:4.4px;line-height:5px;padding:0 10px}

/* four circles */
.col{position:absolute;top:74px;width:70px;text-align:center}
.ring{width:46px;height:46px;border-radius:50%;border:4px solid;margin:0 auto 10px}
.col h4{font-size:6px;font-weight:600;margin-bottom:4px}
.col p{font-size:4.2px;line-height:5.2px;color:var(--mist)}

/* key points */
.kp{position:absolute;top:92px;width:54px;height:54px;border-radius:50%;color:var(--paper);font-size:5px;text-align:center;padding-top:31px;line-height:5px}
.kp-caption{position:absolute;left:70px;right:70px;top:160px;text-align:center;font-size:4.6px;line-height:6px;color:var(--grey)}

/* workflow */
.step{position:absolute;text-align:center;width:44px}
.step b{display:block;font-size:6px;font-weight:600;color:var(--ink);margin-bottom:2px}
.step.red b{color:var(--red)}
.step span{font-size:4.2px;line-height:5px;color:var(--mist)}

/* timeline */
.year{position:absolute;width:40px;height:40px;border-radius:50%;color:var(--paper);text-align:center;padding-top:10px;font-size:8.5px;line-height:9px}
.year small{display:block;font-size:2.8px;line-height:3.2px;padding:1px 10px 0}
.tl-note{position:absolute;font-size:6.4px;color:var(--text)}

/* team */
.member{position:absolute;width:150px}
.member .photo{left:0;top:0;width:42px;height:42px;border-radius:50%;background:radial-gradient(circle at 50% 40%,#d9cfc6,#8d8580)}
.member .info{position:absolute;left:48px;top:2px;width:102px}
.member h5{font-size:7px;font-weight:400;color:var(--ink)}
.member .role{font-size:4px;color:var(--text)}
.member .cred{font-size:4px;color:var(--red)}
.member ul{margin-top:1px;padding-left:6px;font-size:3.8px;line-height:4.6px;color:var(--grey)}

/* testimonials */
.testi-band{left:0;top:115px;width:100%;height:101px;background:var(--ink)}
.testi-pointer{left:103px;top:111px;width:0;height:0;border-left:5px solid transparent;border-right:5px solid transparent;border-bottom:5px solid var(--ink)}
.testi-photo{left:82px;top:44px;width:52px;height:52px;border-radius:50%;background:radial-gradient(circle at 50% 40%,#cfc9c4,#6f6a67)}
.testi-quote{left:165px;top:61px;width:170px;font-size:4.4px;line-height:5.4px;color:var(--grey)}
.testi-quote b{color:var(--text)}
.faq{position:absolute;top:136px;width:60px;text-align:center}
.faq .halo{width:29px;height:29px;border:1.5px solid var(--paper);border-radius:50%;margin:0 auto 7px;display:flex;align-items:center;justify-content:center}
.faq .halo i{width:11px;height:9px;border:1px solid var(--paper);border-radius:1px}
.faq p{font-size:3.7px;line-height:4.4px;color:#ddd}

/* bullets */
.point{position:absolute;left:38px;width:150px}
.point .ico{left:0;top:0;width:16px;height:16px}
.point .body{position:absolute;left:26px;top:1px}
.point .label.hot{color:var(--red)}
.pct{position:absolute;font-size:11px;color:var(--charcoal)}
.legend{left:235px;top:199px;font-size:3.2px;color:var(--grey);display:flex;gap:6px}

/* contact */
.contact .photo{inset:0;background:linear-gradient(115deg,#222 0%,#3b3838 55%,#1e1d1d 100%)}
.contact-panel{left:0;top:0;width:171px;height:216px;background:rgba(20,20,20,.82)}
.contact-band{left:0;top:195px;width:171px;height:21px;background:var(--red);display:flex;justify-content:center;align-items:center;gap:5px}
.contact-band i{width:8px;height:8px;border-radius:50%;background:var(--paper)}
.contact-title{left:52px;top:75px;font-size:17px;font-weight:600;color:var(--paper)}
.contact-list{left:50px;top:108px;list-style:none;font-size:6.8px;color:#eee}
.contact-list li{display:flex;align-items:center;gap:8px;height:17px}
.contact-list svg{width:6px;height:6px;flex:none}
.thanks{left:188px;top:128px;width:180px;text-align:center;color:var(--paper)}
.thanks h2{font-size:20px;font-weight:700;letter-spacing:-.3px}
.thanks p{font-size:6.6px;line-height:8px;color:#ddd}
</style>
</head>
<body>

<!-- 1 Divider -->
<section class="slide divider c1 r1">
  <div class="photo" role="img" aria-label="Dark photo of hands holding a handheld game device"></div>
  <div class="brand light"><span class="brand-dot"></span>PIXELFORGE</div>
  <p class="abs divider-kicker">Divider Page</p>
  <h1 class="abs divider-title">Your Title Goes Here</h1>
  <p class="abs divider-sub">Your Subtitle Here</p>
</section>

<!-- 2 Mock up -->
<section class="slide mockup c2 r1">
  <div class="abs mock-band"></div>
  <h2 class="abs mock-title">Our Mock<br>Up Area</h2>
  <div class="abs mock-screen" role="img" aria-label="Laptop screen showing a child playing a mobile game"></div>
  <div class="abs mock-base"></div>
  <div class="brand"><span class="brand-dot" style="background:#fff"></span>PIXELFORGE</div>
  <div class="feature left" style="left:4px;top:149px"><span class="label">Your Text Here</span><span class="tiny">Lorem ipsum dolor sit amet.</span></div>
  <span class="ico" style="left:132px;top:151px"></span>
  <div class="feature left" style="left:4px;top:178px"><span class="label">Your Text Here</span><span class="tiny">Lorem ipsum dolor sit amet.</span></div>
  <span class="ico" style="left:132px;top:180px"></span>
  <span class="ico" style="left:275px;top:151px"></span>
  <div class="feature" style="left:290px;top:151px"><span class="label">Your Text Here</span><span class="tiny">Lorem ipsum dolor sit amet.</span></div>
  <span class="ico" style="left:275px;top:180px"></span>
  <div class="feature" style="left:290px;top:179px"><span class="label">Your Text Here</span><span class="tiny">Lorem ipsum dolor sit amet.</span></div>
  <div class="footer"><span>© 2017 NORTHPLAY All rights reserved</span><span>38</span></div>
</section>

<!-- 3 Video -->
<section class="slide c3 r1">
  <h2 class="abs video-title">Video Title<br>Goes Here</h2>
  <div class="abs video-copy tiny">
    <p>Lorem ipsum dolor sit amet consectetur adipiscing elit, sed do eiusmod tempor incididunt ut labore et commodo consequat dolore magna aliqua.</p>
    <p>Duis aute irure dolor in reprehenderit in voluptate velit esse cillum dolore eu fugiat nulla pariatur.</p>
    <p>Ut enimad minim veniam, quis nostrud exercitation ullamco laboris.</p>
  </div>
  <div class="abs monitor"><div class="photo" role="img" aria-label="Video still of friends sitting together with tablets"></div></div>
  <div class="abs monitor-neck"></div>
  <div class="abs monitor-foot"></div>
  <div class="brand" style="top:8px"><span class="brand-dot"></span>PIXELFORGE</div>
  <div class="footer"><span>© 2017 NORTHPLAY All rights reserved</span><span>39</span></div>
</section>

<!-- 4 Four column boxes -->
<section class="slide c1 r2">
  <h2 class="slide-title">Four Column Area</h2>
  <div class="brand"><span class="brand-dot"></span>PIXELFORGE</div>
  <p class="lead" style="top:60px">Lorem ipsum dolor sit amet, consectetur adipiscing elit, sed do eiusmod tempor incididunt ut labore et dolore magna aliqua. Ut enimad minim veniam, quis nostrud exercitation ullamco laboris nisi ut aliquip ex ea commodo consequat.</p>
  <div class="box" style="left:30px;background:var(--ink)"><div class="badge"></div><h4>YOUR TEXT HERE</h4><p>Lorem ipsum dolor sit consectetur adipiscing elit.</p></div>
  <div class="box" style="left:115px;background:var(--red)"><div class="badge"></div><h4>YOUR TEXT HERE</h4><p>Lorem ipsum dolor sit consectetur adipiscing elit.</p></div>
  <div class="box" style="left:199px;background:var(--charcoal)"><div class="badge"></div><h4>YOUR TEXT HERE</h4><p>Lorem ipsum dolor sit consectetur adipiscing elit.</p></div>
  <div class="box" style="left:284px;background:var(--stone)"><div class="badge"></div><h4>YOUR TEXT HERE</h4><p>Lorem ipsum dolor sit consectetur adipiscing elit.</p></div>
  <div class="footer"><span>© 2017 NORTHPLAY All rights reserved</span><span>40</span></div>
</section>

<!-- 5 Four column circles -->
<section class="slide c2 r2">
  <h2 class="slide-title">Four Column Area</h2>
  <div class="brand"><span class="brand-dot"></span>PIXELFORGE</div>
  <p class="lead" style="top:49px;text-align:center">Lorem ipsum dolor sit amet, consectetur adipiscing elit, sed do eiusmod tempor incididunt ut labore et dolore magna aliqua. Ut enim minim veniam, quis nostrud exercitation ullamco laboris nisi ut aliquip ex ea commodo consequat.</p>
  <div class="col" style="left:41px"><div class="ring" style="border-color:var(--ink)"></div><h4>COLUMN 1</h4><p>Lorem ipsum dolor sit amet, consectetur adipiscing elit, sed do eiusmod tempor incididunt ut labore et dolore magna aliqua.</p></div>
  <div class="col" style="left:119px"><div class="ring" style="border-color:var(--red)"></div><h4 style="color:var(--red)">COLUMN 2</h4><p>Lorem ipsum dolor sit amet, consectetur adipiscing elit, sed do eiusmod tempor incididunt ut labore et dolore magna aliqua.</p></div>
  <div class="col" style="left:196px"><div class="ring" style="border-color:var(--charcoal)"></div><h4>COLUMN 3</h4><p>Lorem ipsum dolor sit amet, consectetur adipiscing elit, sed do eiusmod tempor incididunt ut labore et dolore magna aliqua.</p></div>
  <div class="col" style="left:273px"><div class="ring" style="border-color:var(--grey)"></div><h4 style="color:var(--stone)">COLUMN 4</h4><p>Lorem ipsum dolor sit amet, consectetur adipiscing elit, sed do eiusmod tempor incididunt ut labore et dolore magna aliqua.</p></div>
  <div class="footer"><span>© 2017 NORTHPLAY All rights reserved</span><span>41</span></div>
</section>

<!-- 6 Key points -->
<section class="slide c3 r2">
  <h2 class="slide-title">Key Points Area</h2>
  <div class="brand"><span class="brand-dot"></span>PIXELFORGE</div>
  <p class="lead" style="left:24px;top:62px">Lorem ipsum dolor sit amet, consectetur adipiscing elit, sed do eiusmod tempor incididunt ut labore et dolore magna aliqua. Ut enim minim veniam, quis nostrud exercitation ullamco laboris nisi ut aliquip ex ea commodo consequat.</p>
  <div class="kp" style="left:73px;background:var(--ink)">Lorem<br>ipsum</div>
  <div class="kp" style="left:119px;background:var(--rose)">Lorem<br>ipsum</div>
  <div class="kp" style="left:165px;background:var(--charcoal)">Lorem<br>ipsum</div>
  <div class="kp" style="left:211px;background:var(--rose)">Lorem<br>ipsum</div>
  <div class="kp" style="left:257px;background:var(--ink)">Lorem<br>ipsum</div>
  <p class="kp-caption">Lorem ipsum dolor sit amet, consectetur adipiscing elit, sed do eiusmod tempor incididunt ut labore et dolore magna aliqua. Ut enim minim veniam, quis nostrud exercitation ullamco laboris nisi ut aliquip ex ea commodo consequat.</p>
  <div class="footer"><span>© 2017 NORTHPLAY All rights reserved</span><span>42</span></div>
</section>

<!-- 7 Workflow -->
<section class="slide c1 r3">
  <h2 class="slide-title">Workflow Area</h2>
  <div class="brand"><span class="brand-dot"></span>PIXELFORGE</div>
  <p class="lead" style="left:29px;top:59px">Lorem ipsum dolor sit amet, consectetur adipiscing elit, sed do eiusmod tempor incididunt ut labore et dolore magna aliqua. Ut enim minim veniam, quis nostrud exercitation ullamco laboris nisi ut aliquip ex ea commodo consequat.</p>
  <svg class="abs" style="left:0;top:0" width="383" height="216" viewBox="0 0 383 216" aria-hidden="true">
    <g fill="none" stroke-width="12">
      <path d="M33 124 A32 32 0 0 1 97 124" stroke="#111"/>
      <path d="M97 124 A32 32 0 0 0 161 124" stroke="#c41230"/>
      <path d="M161 124 A32 32 0 0 1 225 124" stroke="#111"/>
      <path d="M225 124 A32 32 0 0 0 289 124" stroke="#c41230"/>
      <path d="M289 124 A32 32 0 0 1 353 124" stroke="#111"/>
    </g>
    <g font-family="Montserrat,sans-serif" font-size="5" text-anchor="middle" fill="#fff">
      <circle cx="65" cy="119" r="5.5" fill="#111"/><text x="65" y="121">1</text>
      <circle cx="129" cy="137" r="5.5" fill="#c41230"/><text x="129" y="139">2</text>
      <circle cx="193" cy="119" r="5.5" fill="#111"/><text x="193" y="121">3</text>
      <circle cx="257" cy="137" r="5.5" fill="#c41230"/><text x="257" y="139">4</text>
      <circle cx="321" cy="119" r="5.5" fill="#111"/><text x="321" y="121">5</text>
    </g>
  </svg>
  <div class="step" style="left:43px;top:128px"><b>Data 1</b><span>Lorem ipsum dolor sit amet, consectetur adipiscing elit.</span></div>
  <div class="step red" style="left:107px;top:88px"><b>Data 2</b><span>Lorem ipsum dolor sit amet, consectetur adipiscing elit.</span></div>
  <div class="step" style="left:171px;top:128px"><b>Data 3</b><span>Lorem ipsum dolor sit amet, consectetur adipiscing elit.</span></div>
  <div class="step red" style="left:235px;top:88px"><b>Data 4</b><span>Lorem ipsum dolor sit amet, consectetur adipiscing elit.</span></div>
  <div class="step" style="left:299px;top:128px"><b>Data 5</b><span>Lorem ipsum dolor sit amet, consectetur adipiscing elit.</span></div>
  <div class="footer"><span>© 2017 NORTHPLAY All rights reserved</span><span>43</span></div>
</section>

<!-- 8 Timeline -->
<section class="slide c2 r3">
  <h2 class="slide-title">Timeline</h2>
  <div class="brand"><span class="brand-dot"></span>PIXELFORGE</div>
  <svg class="abs" style="left:0;top:0" width="383" height="216" viewBox="0 0 383 216" aria-hidden="true">
    <g stroke="#b3b3b3" stroke-width=".8">
      <line x1="52" y1="101" x2="338" y2="101"/>
      <line x1="98" y1="82" x2="98" y2="101"/><line x1="144" y1="101" x2="144" y2="120"/>
      <line x1="190" y1="82" x2="190" y2="101"/><line x1="236" y1="101" x2="236" y2="120"/>
      <line x1="282" y1="82" x2="282" y2="101"/>
    </g>
    <circle cx="328" cy="101" r="22.5" fill="none" stroke="#c41230" stroke-width="1.5" stroke-dasharray="40 200"/>
  </svg>
  <div class="year" style="left:32px;top:81px;background:var(--ink)">2012<small>Your Text Goes Here</small></div>
  <div class="year" style="left:78px;top:42px;background:var(--red)">2013<small>Your Text Goes Here</small></div>
  <div class="year" style="left:124px;top:120px;background:var(--charcoal)">2014<small>Your Text Goes Here</small></div>
  <div class="year" style="left:170px;top:42px;background:var(--grey)">2015<small>Your Text Goes Here</small></div>
  <div class="year" style="left:216px;top:120px;background:var(--grey)">2016<small>Your Text Goes Here</small></div>
  <div class="year" style="left:262px;top:42px;background:var(--red)">2017<small>Your Text Goes Here</small></div>
  <div class="year" style="left:308px;top:81px;background:var(--ink)">2018<small>Your Text Goes Here</small></div>
  <div class="tl-note" style="left:272px;top:139px;width:95px;text-align:right">Your Text Goes Here<div class="tiny">Lorem ipsum dolor sit amet, consectetur adipiscing elit, sed do eiusmod tempor incididunt ut labore et dolore magna aliqua.</div></div>
  <div class="tl-note" style="left:17px;top:174px;width:170px">Your Text Goes Here<div class="tiny">Lorem ipsum dolor sit amet, consectetur adipiscing elit, sed do eiusmod tempor incididunt ut labore et dolore magna aliqua.</div></div>
  <div class="footer"><span>© 2017 NORTHPLAY All rights reserved</span><span>44</span></div>
</section>

<!-- 9 Team -->
<section class="slide c3 r3">
  <h2 class="slide-title">Our Team</h2>
  <div class="brand"><span class="brand-dot"></span>PIXELFORGE</div>
  <div class="member" style="left:24px;top:54px">
    <div class="photo" role="img" aria-label="Portrait photo of team member"></div>
    <div class="info"><h5>Michael Doe</h5><p class="role">CEO</p><p class="cred">MSc, MBA and CIM Dip PM</p>
      <ul><li>Lorem ipsum dolor sit amet, consectetur adipiscing elit</li><li>sed do eiusmod tempor incididunt ut labore et dolore magna aliqua</li><li>Ut enim minim veniam, quis nostrud exercitation</li></ul></div>
  </div>
  <div class="member" style="left:195px;top:54px">
    <div class="photo" role="img" aria-label="Portrait photo of team member"></div>
    <div class="info"><h5>James Doe</h5><p class="role">Manager</p><p class="cred">M.B.A</p>
      <ul><li>Lorem ipsum dolor sit amet, consectetur adipiscing elit</li><li>sed do eiusmod tempor incididunt ut labore et dolore magna aliqua</li><li>Ut enim minim veniam, quis nostrud exercitation</li></ul></div>
  </div>
  <div class="member" style="left:24px;top:127px">
    <div class="photo" role="img" aria-label="Portrait photo of team member"></div>
    <div class="info"><h5>Jane Doe</h5><p class="role">Doctor of Chemistry</p><p class="cred">M.B.A</p>
      <ul><li>Lorem ipsum dolor sit amet, consectetur adipiscing elit</li><li>sed do eiusmod tempor incididunt ut labore et dolore magna aliqua</li><li>Ut enim minim veniam, quis nostrud exercitation</li></ul></div>
  </div>
  <div class="member" style="left:195px;top:127px">
    <div class="photo" role="img" aria-label="Portrait photo of team member"></div>
    <div class="info"><h5>John Doe</h5><p class="role">Doctor of Physical</p><p class="cred">Professor</p>
      <ul><li>Lorem ipsum dolor sit amet, consectetur adipiscing elit</li><li>sed do eiusmod tempor incididunt ut labore et dolore magna aliqua</li><li>Ut enim minim veniam, quis nostrud exercitation</li></ul></div>
  </div>
  <div class="footer"><span>© 2017 NORTHPLAY All rights reserved</span><span>45</span></div>
</section>

<!-- 10 Testimonials -->
<section class="slide c1 r4">
  <h2 class="slide-title">Customer Testimonials</h2>
  <div class="brand"><span class="brand-dot"></span>PIXELFORGE</div>
  <div class="abs testi-photo" role="img" aria-label="Portrait photo of a customer"></div>
  <p class="abs testi-quote">adipiscing elit, sed diam nonummy nibh euismod tincidunt ut laoreet dolore magna aliquam erat volutpat. Ut wisi enim <b>Lorem ipsum</b> dolor sit amet, consectetuer adipiscing elit, sed diam nonummy nibh euismod tincidunt ut laoreet dolore magna</p>
  <div class="abs testi-band"></div>
  <div class="abs testi-pointer"></div>
  <div class="faq" style="left:69px"><div class="halo"><i></i></div><p>Why does getting a loan have to be so much more complicated than ordering a fridge online?</p></div>
  <div class="faq" style="left:141px"><div class="halo"><i></i></div><p>Why do I have to go to a branch, fill out forms and wait for weeks to get a response?</p></div>
  <div class="faq" style="left:214px"><div class="halo"><i></i></div><p>Why do banks refuse to lend to me despite the substantial fees I receive each month?</p></div>
  <div class="faq" style="left:287px"><div class="halo"><i></i></div><p>Why is there no online shop in banking that identifies my needs and offers convenience at fair prices?</p></div>
</section>

<!-- 11 Bullets & chart -->
<section class="slide c2 r4">
  <h2 class="slide-title">Bullet &amp; Chart Area</h2>
  <div class="brand"><span class="brand-dot"></span>PIXELFORGE</div>
  <div class="point" style="top:64px"><span class="ico"></span><div class="body"><span class="label">Your Text Here</span><div class="tiny">Lorem ipsum dolor sit amet, consectetur<br>adipiscing elit, sed do eiusmod.</div></div></div>
  <div class="point" style="top:96px"><span class="ico" style="background:var(--red)"></span><div class="body"><span class="label hot">Your Text Here</span><div class="tiny">Lorem ipsum dolor sit amet, consectetur<br>adipiscing elit, sed do eiusmod.</div></div></div>
  <div class="point" style="top:127px"><span class="ico" style="background:var(--charcoal)"></span><div class="body"><span class="label">Your Text Here</span><div class="tiny">Lorem ipsum dolor sit amet, consectetur<br>adipiscing elit, sed do eiusmod.</div></div></div>
  <div class="point" style="top:158px"><span class="ico" style="background:var(--grey)"></span><div class="body"><span class="label">Your Text Here</span><div class="tiny">Lorem ipsum dolor sit amet, consectetur<br>adipiscing elit, sed do eiusmod.</div></div></div>
  <svg class="abs" style="left:232px;top:74px" width="90" height="90" viewBox="0 0 90 90" aria-hidden="true">
    <g transform="rotate(-90 45 45)" fill="none" stroke-width="13">
      <circle cx="45" cy="45" r="38" stroke="#111" stroke-dasharray="142.3 238.8"/>
      <circle cx="45" cy="45" r="38" stroke="#c41230" stroke-dasharray="58.7 238.8" stroke-dashoffset="-143.3"/>
      <circle cx="45" cy="45" r="38" stroke="#3b3939" stroke-dasharray="34.8 238.8" stroke-dashoffset="-203"/>
      <circle cx="45" cy="45" r="38" stroke="#6b6464" stroke-dasharray="22.9 238.8" stroke-dashoffset="-238.8"/>
    </g>
    <g fill="#9a9a9a"><rect x="34" y="50" width="3" height="5"/><rect x="39" y="46" width="3" height="9"/><rect x="44" y="41" width="3" height="14"/><rect x="49" y="35" width="3" height="20"/></g>
    <line x1="31" y1="55.5" x2="55" y2="55.5" stroke="#9a9a9a" stroke-width="1"/>
  </svg>
  <span class="pct" style="left:254px;top:58px">10%</span>
  <span class="pct" style="left:207px;top:88px">15%</span>
  <span class="pct" style="left:207px;top:141px">25%</span>
  <span class="pct" style="left:329px;top:114px">60%</span>
  <div class="abs legend"><span>● 1st Qtr</span><span>● 2nd Qtr</span><span>● 3rd Qtr</span><span>● 4th Qtr</span></div>
  <div class="footer"><span>© 2017 NORTHPLAY All rights reserved</span><span>47</span></div>
</section>

<!-- 12 Contact -->
<section class="slide contact c3 r4">
  <div class="photo" role="img" aria-label="Dark photo of a person playing a video game"></div>
  <div class="abs contact-panel"></div>
  <div class="brand light" style="left:58px;right:auto;top:47px;font-size:8px"><span class="brand-dot"></span>PIXELFORGE</div>
  <h2 class="abs contact-title">Our Contact</h2>
  <ul class="abs contact-list">
    <li><svg viewBox="0 0 10 10"><path d="M5 1 L9.5 5 H8 V9 H2 V5 H.5 Z" fill="#fff"/></svg><span>123 Street Road<br>City 12345</span></li>
    <li><svg viewBox="0 0 10 10"><path d="M2 1 L4 1 L5 3.5 L3.7 4.5 Q5 6.5 5.6 6.3 L6.5 5 L9 6 L9 8 Q5 9.5 1 2 Z" fill="#fff"/></svg><span>(123) 456-7890</span></li>
    <li><svg viewBox="0 0 10 10"><rect x="1" y="2" width="8" height="6" fill="#fff"/><path d="M1 2 L5 5.5 L9 2" stroke="#222" fill="none" stroke-width=".8"/></svg><span>emailaddress@email.com</span></li>
    <li><svg viewBox="0 0 10 10"><circle cx="5" cy="5" r="4" fill="#fff"/><path d="M1 5 H9 M5 1 V9" stroke="#222" stroke-width=".7"/></svg><span>www.website-address.com</span></li>
  </ul>
  <div class="abs contact-band"><i></i><i></i><i></i></div>
  <div class="abs thanks"><h2>THANK YOU</h2><p style="font-size:7.5px;margin:1px 0 6px">For Your Precious Time</p><p>Stop by our office or give us a call!<br>We would love to hear from you.</p></div>
</section>

</body>
</html>
```